Stonelynk Business Card Design

The Stonelynk Co is an aggregate (crushing) equipment dealer serving Western Canadian provinces. Stonelynk is a distributor of aggregate equipment for different manufacturers.

We are looking to change and update the existing business card which has been used since the existence of the company. A copy of existing card has been attached for reference. The Stonelynk Co logo we want to remain the same and we want the green color to remain the same.

We are wanting something new with a different look. A refreshing card to show a new modern and updated look. No longer wanting to have the manufacturers on the back of the card but something more like our logo on the back of the card with a statement like "Crushing Solutions"

ideas could be:
- card can be different colors on front and back
- front or reverse of the card could possibly be the green color with the logo in black

Target Market(s)

Owners of Aggregate/Crushing companies

Requirements
Must have
• - logo to remain same along with same font within logo
• - green color to remain same
Nice to have
• as noted above under project description
Should not have

```html
<!DOCTYPE html>
<html lang="en">
<head>
<meta charset="utf-8">
<title>The Stonelynk Co – Business Card</title>
<link href="https://fonts.googleapis.com/css2?family=Montserrat:wght@400;500;700;800&display=swap" rel="stylesheet">
<style>
  :root {
    --olive: #8c9b10;
    --olive-dark: #7a8a0c;
    --charcoal: #231f20;
    --charcoal-soft: #2d292a;
    --paper: #ffffff;
    --mist: #ecebe2;
    --stage: #a3a3a3;
    --ink: #1e1b1c;
  }
  * { box-sizing: border-box; margin: 0; padding: 0; }
  html, body { width: 1200px; height: 1200px; overflow: hidden; }
  body {
    background: var(--stage);
    font-family: "Montserrat", Arial, sans-serif;
    display: flex;
    align-items: center;
    justify-content: center;
    gap: 40px;
  }
  .card {
    position: relative;
    width: 540px;
    height: 325px;
    overflow: hidden;
    box-shadow: 0 2px 6px rgba(0,0,0,0.25);
  }

  /* ---------- Front ---------- */
  .card-front { background: var(--charcoal); }
  .front-top {
    position: absolute; left: 0; top: 0; width: 100%; height: 143px;
    background: var(--paper);
  }
  .front-top .faint-decoration {
    position: absolute; right: 0; top: 0; width: 230px; height: 143px;
    background: radial-gradient(ellipse at 70% 40%, var(--mist) 0%, rgba(236,235,226,0.6) 45%, rgba(255,255,255,0) 75%);
  }
  .divider { position: absolute; left: 0; top: 136px; width: 100%; height: 16px; }
  .front-bottom {
    position: absolute; left: 0; top: 148px; width: 100%; height: 177px;
    background:
      repeating-linear-gradient(45deg, rgba(255,255,255,0.018) 0 2px, transparent 2px 4px),
      var(--charcoal);
  }
  .brand {
    position: absolute; left: 26px; top: 28px;
    display: flex; align-items: center; gap: 14px;
  }
  .brand-dot { width: 42px; height: 42px; border-radius: 50%; background: var(--olive); }
  .brand-name {
    font-weight: 800; font-size: 17px; letter-spacing: 0.3px; color: var(--ink);
  }
  .tagline {
    position: absolute; left: 188px; top: 68px;
    font-size: 9px; letter-spacing: 1.4px; color: var(--olive); font-weight: 500;
  }
  .contact-list {
    position: absolute; left: 22px; top: 170px;
    list-style: none; color: var(--paper); font-size: 14px; line-height: 1.2;
  }
  .contact-list li { display: flex; align-items: center; gap: 10px; margin-bottom: 9px; }
  .contact-list li.address { align-items: flex-start; margin-bottom: 13px; }
  .icon-circle {
    flex: none; width: 21px; height: 21px; border-radius: 50%;
    background: var(--olive); display: flex; align-items: center; justify-content: center;
  }
  .person {
    position: absolute; right: 0; top: 164px; width: 185px; padding-left: 4px;
    font-size: 18px; letter-spacing: 0.5px; color: var(--paper);
  }
  .person strong { font-weight: 700; }
  .person-rule { display: block; margin-top: 4px; height: 2px; background: var(--olive); }
  .online-list {
    position: absolute; right: 24px; top: 241px;
    list-style: none; color: var(--paper); font-size: 14px; letter-spacing: 0.4px;
  }
  .online-list li { display: flex; align-items: center; justify-content: flex-end; gap: 14px; margin-bottom: 10px; }
  .icon-square {
    flex: none; width: 20px; height: 20px; border-radius: 4px;
    background: var(--olive); display: flex; align-items: center; justify-content: center;
  }

  /* ---------- Back ---------- */
  .card-back { background: var(--olive); }
  .card-back .faint-decoration {
    position: absolute; right: -40px; bottom: 0; width: 380px; height: 150px;
    background: radial-gradient(ellipse at 65% 70%, rgba(160,176,40,0.8) 0%, rgba(160,176,40,0.35) 50%, rgba(140,155,16,0) 75%);
  }
  .back-brand {
    position: absolute; left: 0; right: 0; top: 138px;
    display: flex; align-items: center; justify-content: center; gap: 16px;
  }
  .back-brand .brand-dot { width: 40px; height: 40px; background: var(--ink); }
  .back-brand .brand-name { font-size: 19px; color: var(--ink); }
  .web-band {
    position: absolute; left: 0; top: 277px; width: 100%; height: 18px;
    background: linear-gradient(90deg, rgba(35,31,32,0) 0%, var(--charcoal) 22%, var(--charcoal) 70%, rgba(35,31,32,0.9) 85%, rgba(35,31,32,0) 100%);
    color: var(--paper); font-size: 10px; letter-spacing: 1.6px;
    display: flex; align-items: center; justify-content: center;
  }
</style>
</head>
<body>

  <section class="card card-front" aria-label="Business card front">
    <div class="front-top">
      <div class="faint-decoration" role="img" aria-label="Soft pale background shading"></div>
      <div class="brand">
        <span class="brand-dot"></span>
        <span class="brand-name">THE STONELYNK CO.</span>
      </div>
      <p class="tagline">SCREENERS &nbsp;|&nbsp; CRUSHERS &nbsp;|&nbsp; STACKERS</p>
    </div>

    <div class="front-bottom"></div>
    <svg class="divider" viewBox="0 0 540 16" preserveAspectRatio="none" aria-hidden="true">
      <polygon points="0,10 170,10 176,2 182,2 176,10 540,10 540,14 0,14" fill="var(--olive)"/>
    </svg>

    <ul class="contact-list">
      <li class="address">
        <span class="icon-circle">
          <svg width="11" height="13" viewBox="0 0 11 13" aria-hidden="true"><path d="M5.5 0.8a4 4 0 0 0-4 4c0 3 4 7.4 4 7.4s4-4.4 4-7.4a4 4 0 0 0-4-4z" fill="none" stroke="#fff" stroke-width="1.1"/><circle cx="5.5" cy="4.8" r="1.4" fill="#fff"/></svg>
        </span>
        <span>2218-48B AVENUE NISKU,<br>ALBERTA T9E1K7</span>
      </li>
      <li>
        <span class="icon-circle">
          <svg width="12" height="12" viewBox="0 0 12 12" aria-hidden="true"><path d="M2.6 1.2l1.8 2.1-1 1.3a7 7 0 0 0 4 4l1.3-1 2.1 1.8-1 1.6C5.5 11 1 6.5 1 2.2z" fill="none" stroke="#fff" stroke-width="1"/></svg>
        </span>
        <span>780.555.0142</span>
      </li>
      <li>
        <span class="icon-circle">
          <svg width="12" height="12" viewBox="0 0 12 12" aria-hidden="true"><path d="M2.6 1.2l1.8 2.1-1 1.3a7 7 0 0 0 4 4l1.3-1 2.1 1.8-1 1.6C5.5 11 1 6.5 1 2.2z" fill="none" stroke="#fff" stroke-width="1"/></svg>
        </span>
        <span>780.555.0178</span>
      </li>
      <li>
        <span class="icon-circle">
          <svg width="12" height="12" viewBox="0 0 12 12" aria-hidden="true"><rect x="2" y="5" width="8" height="5.5" fill="none" stroke="#fff" stroke-width="1"/><rect x="3.5" y="1.5" width="5" height="3.5" fill="none" stroke="#fff" stroke-width="1"/></svg>
        </span>
        <span>780.555.0193</span>
      </li>
    </ul>

    <p class="person"><strong>DALE</strong> MORROW<span class="person-rule"></span></p>

    <ul class="online-list">
      <li>
        <span>DALE@STONELYNK.COM</span>
        <span class="icon-square">
          <svg width="12" height="9" viewBox="0 0 12 9" aria-hidden="true"><rect x="0.6" y="0.6" width="10.8" height="7.8" fill="none" stroke="#fff" stroke-width="1"/><path d="M0.8 0.8L6 5l5.2-4.2" fill="none" stroke="#fff" stroke-width="1"/></svg>
        </span>
      </li>
      <li>
        <span>WWW.STONELYNK.CA</span>
        <span class="icon-square">
          <svg width="12" height="12" viewBox="0 0 12 12" aria-hidden="true"><circle cx="6" cy="6" r="5" fill="none" stroke="#fff" stroke-width="1"/><ellipse cx="6" cy="6" rx="2.2" ry="5" fill="none" stroke="#fff" stroke-width="0.9"/><path d="M1 6h10" stroke="#fff" stroke-width="0.9"/></svg>
        </span>
      </li>
    </ul>
  </section>

  <section class="card card-back" aria-label="Business card back">
    <div class="faint-decoration" role="img" aria-label="Soft lighter green background shading"></div>
    <div class="back-brand">
      <span class="brand-dot"></span>
      <span class="brand-name">THE STONELYNK CO.</span>
    </div>
    <div class="web-band">WWW.STONELYNK.CA</div>
  </section>

</body>
</html>
```